Tasman Curdworks Guild needs new business cards

We need new business cards designed and produced. We are likely to need other design work done for ads, flyers etc in future.

We would like to start with an initial business card.

The Tasman Curdworks Guild (TCG) is a membership-based not-for-profit organisation that looks after the interests of Australia's small to medium artisan cheesemakers, many of whom are also small-scale farmers. The design should be simple, using our logo, but also communicate our artisan cheese and small dairy farm focus.

The first card to be designed and produced is for me, Miriam Tolhurst. My details are:

Miriam Tolhurst
Secretary
Tasman Curdworks Guild (TCG)
http://www.curdworksguild.example
T +61452837190
E miriam.miriamtolhurst@mailbox.example

I have attached the TCG logo in jpg form. I have a higher resolution version available if needed.

Thank you!

Miriam

Miriam Tolhurst
Tasman Curdworks Guild
miriam.miriamtolhurst@mailbox.example
+61452837190

Sans Serif

• Logo (see attached file)

```html
<!DOCTYPE html>
<html lang="en">
<head>
<meta charset="utf-8">
<title>Tasman Curdworks Guild — Business Card</title>
<link rel="stylesheet" href="https://fonts.googleapis.com/css2?family=Tinos:wght@400;700&display=swap">
<style>
  :root {
    --backdrop: #232323;
    --card-white: #ffffff;
    --cheese: #fdcb6a;
    --brown: #5a3a1c;
    --ink: #1f1a16;
    --text-brown: #4a3a2a;
    --farm-grey: #e3e3e3;
    --gold: #f2b93f;
  }
  html, body {
    margin: 0;
    width: 1200px;
    height: 852px;
    overflow: hidden;
    background: var(--backdrop);
    font-family: "Tinos", "Times New Roman", serif;
  }
  .card {
    position: absolute;
    width: 560px;
    height: 330px;
    border-radius: 22px;
    overflow: hidden;
    background: var(--card-white);
    box-shadow: 0 10px 30px rgba(0,0,0,.45);
  }
  .card-front { left: 90px; top: 70px; }
  .card-back  { left: 550px; top: 450px; }
  .card-art { position: absolute; inset: 0; }

  .guild-mark {
    position: absolute;
    display: flex;
    align-items: center;
    gap: 18px;
  }
  .guild-mark .mark-disc {
    flex: none;
    border-radius: 50%;
    background: var(--card-white);
    border: 2px solid var(--brown);
  }
  .guild-name {
    color: var(--text-brown);
    font-weight: 400;
    line-height: 0.95;
  }
  .card-front .guild-mark { left: 38px; top: 150px; }
  .card-front .mark-disc { width: 150px; height: 150px; border: none; }
  .card-front .guild-name { font-size: 34px; }

  .card-back .guild-mark { left: 40px; top: 78px; }
  .card-back .mark-disc { width: 66px; height: 66px; }
  .card-back .guild-name { font-size: 24px; }

  .contact-block { position: absolute; left: 48px; top: 200px; color: var(--ink); }
  .person-name { font-size: 27px; font-weight: 700; margin: 0; }
  .person-role { font-size: 14px; margin: 2px 0 10px; color: var(--text-brown); }
  .contact-list { list-style: none; margin: 0; padding: 0; font-size: 15px; }
  .contact-list li { display: flex; align-items: center; gap: 10px; height: 22px; }
  .contact-icon { width: 17px; height: 17px; flex: none; }
</style>
</head>
<body>

<section class="card card-front" aria-label="Card front">
  <svg class="card-art" viewBox="0 0 560 330" aria-hidden="true">
    <path fill="var(--cheese)" d="M0 175 C70 160 80 60 190 45 C260 35 285 0 330 0 L560 0 L560 330 L0 330 Z"/>
    <circle cx="395" cy="85" r="38" fill="var(--card-white)"/>
    <circle cx="505" cy="250" r="42" fill="var(--card-white)"/>
  </svg>
  <div class="guild-mark">
    <span class="mark-disc"></span>
    <span class="guild-name">Tasman<br>Curdworks<br>Guild</span>
  </div>
</section>

<section class="card card-back" aria-label="Card back">
  <svg class="card-art" viewBox="0 0 560 330" aria-hidden="true">
    <defs>
      <linearGradient id="farmTone" x1="0" x2="1">
        <stop offset="0" stop-color="var(--farm-grey)" stop-opacity="0.6"/>
        <stop offset="1" stop-color="var(--farm-grey)"/>
      </linearGradient>
    </defs>
    <path fill="var(--cheese)" d="M270 0 L560 0 L560 80 C500 120 420 130 360 110 C320 95 300 70 290 40 Z"/>
    <path fill="none" stroke="var(--brown)" stroke-width="3" d="M275 45 C300 110 420 140 560 90"/>
    <circle cx="315" cy="30" r="16" fill="var(--card-white)"/>
    <circle cx="405" cy="55" r="30" fill="var(--card-white)"/>
  </svg>
  <svg class="card-art" viewBox="0 0 560 330" role="img" aria-label="Faint grey illustration of a farmhouse and a grazing dairy cow">
    <path fill="url(#farmTone)" d="M150 200 L190 140 L260 130 L300 150 L380 110 L470 95 L560 110 L560 240 L150 240 Z"/>
  </svg>
  <div class="guild-mark">
    <span class="mark-disc"></span>
    <span class="guild-name">Tasman<br>Curdworks<br>Guild</span>
  </div>
  <div class="contact-block">
    <h1 class="person-name">Miriam Tolhurst</h1>
    <p class="person-role">Secretary</p>
    <ul class="contact-list">
      <li>
        <svg class="contact-icon" viewBox="0 0 20 20" aria-hidden="true"><circle cx="10" cy="10" r="10" fill="var(--gold)"/><path d="M6 5 L8 5 L9 8 L8 9 C9 11 10 12 11 12 L12 11 L15 12 L15 14 C12 15 5 9 6 5 Z" fill="var(--brown)"/></svg>
        <span>+61452837190</span>
      </li>
      <li>
        <svg class="contact-icon" viewBox="0 0 20 20" aria-hidden="true"><circle cx="10" cy="10" r="10" fill="var(--gold)"/><rect x="5" y="6.5" width="10" height="7" fill="none" stroke="var(--brown)" stroke-width="1.4"/><path d="M5 6.5 L10 10.5 L15 6.5" fill="none" stroke="var(--brown)" stroke-width="1.4"/></svg>
        <span>miriam.miriamtolhurst@mailbox.example</span>
      </li>
      <li>
        <svg class="contact-icon" viewBox="0 0 20 20" aria-hidden="true"><circle cx="10" cy="10" r="10" fill="var(--gold)"/><circle cx="10" cy="10" r="5" fill="none" stroke="var(--brown)" stroke-width="1.3"/><path d="M5 10 H15 M10 5 C7 8 7 12 10 15 M10 5 C13 8 13 12 10 15" fill="none" stroke="var(--brown)" stroke-width="1.1"/></svg>
        <span>www.curdworksguild.example</span>
      </li>
    </ul>
  </div>
</section>

</body>
</html>
```